Move the hackers to Wordpress

Yep, we want to move https://www.tallowmarsh.com/ to Wordpress. It'll make it easier to update and add content. I'd like mostly the same look, but I'm not stuck with it.
Updates

DO NOT RESPOND OUTSIDE OF PIXEL HARBOR OR CONTACT US DIRECTLY.

Industry/Entity Type

Computer Security

Coding

Coded - Design and coding required

Font styles to use
Sans Serif

Colors
ec1f27

Requirements
Must have
• What I do want is:
• 1. Similar look to the existing site
• 2. Needs to work on one of the Wordpress hosting sites. I do NOT want to run my own Wordpress server.
• 3. Keep the animation in the top panel.
• 4. Mobile support
• The rest can be changed as needed.
Nice to have
• I like the transitions when the "services" panel shows up. Not stuck on it, but it is a nice touch.

```html
<!DOCTYPE html>
<html lang="en">
<head>
<meta charset="utf-8">
<title>Tallow Marsh — Offensive Security</title>
<link href="https://fonts.googleapis.com/css2?family=Lato:wght@400;700;900&display=swap" rel="stylesheet">
<style>
:root{
  --red:#ec1f27;
  --red-dark:#c5161d;
  --charcoal:#2b2b2b;
  --charcoal-2:#343434;
  --grey:#8c8c8c;
  --grey-light:#a3a3a3;
  --paper:#efefef;
  --white:#ffffff;
  --ink:#333333;
}
*{box-sizing:border-box;margin:0;padding:0}
html,body{width:1200px;height:3412px;overflow:hidden}
body{font-family:"Lato",Arial,sans-serif;background:var(--charcoal);color:var(--white);position:relative}
.page{position:relative;width:1200px;height:3412px;overflow:hidden}

/* hero */
.hero{position:absolute;left:0;top:0;width:1200px;height:470px;background:var(--charcoal)}
.hero-bg{position:absolute;inset:0}
.brand{position:absolute;left:44px;top:26px;display:flex;align-items:center;gap:10px;font-weight:900;font-size:30px;color:var(--red);letter-spacing:1px}
.brand-square{width:22px;height:22px;background:var(--red)}
.nav{position:absolute;right:60px;top:38px;display:flex;gap:40px;font-size:14px;font-weight:700;letter-spacing:1px}
.nav a{color:var(--white);text-decoration:none}
.nav a.active{color:var(--red)}
.headline{position:absolute;left:0;top:140px;width:1200px;text-align:center;font-weight:900;font-size:82px;line-height:86px;text-transform:uppercase;color:var(--white)}
.headline .hl{color:var(--red)}

/* what we do */
.about{position:absolute;left:0;top:400px;width:1200px;height:560px;background:var(--grey)}
.about-shapes{position:absolute;inset:0}
.about h2{position:absolute;left:120px;top:60px;font-size:48px;font-weight:900}
.about-copy{position:absolute;left:120px;top:130px;width:680px;font-size:17px;line-height:26px}
.about-copy p{margin-bottom:22px}
.about-copy .lead{font-weight:700}
.about-mark{position:absolute;left:860px;top:160px;display:flex;flex-direction:column;align-items:center;gap:14px;font-weight:900;font-size:26px;color:var(--red)}
.about-mark .sq{width:110px;height:110px;background:var(--red)}

/* services */
.services{position:absolute;left:0;top:940px;width:1200px;height:1330px;background:var(--red)}
.services-shape{position:absolute;inset:0}
.services h2{position:absolute;left:120px;top:50px;font-size:48px;font-weight:900}
.grid{position:absolute;left:120px;top:150px;width:960px;display:grid;grid-template-columns:repeat(3,1fr);column-gap:60px;row-gap:80px}
.card{text-align:center}
.card svg{width:100px;height:100px;margin:0 auto 34px;display:block}
.card h3{font-size:17px;font-weight:900;line-height:22px;min-height:44px;margin-bottom:14px}
.card p{font-size:16px;line-height:25px;text-align:justify}

/* testimonial */
.testimonial{position:absolute;left:0;top:2200px;width:1200px;height:780px;background:var(--paper)}
.quote-mark{position:absolute;top:230px;font-family:"Lato",Georgia,serif;font-weight:900;font-size:300px;line-height:1;color:#c4c4c4}
.quote-mark.left{left:110px}
.quote-mark.right{right:110px}
.avatar{position:absolute;left:520px;top:170px;width:160px;height:160px;border-radius:50%;background:radial-gradient(circle at 50% 40%,#7fbf7a,#4e9a4c)}
.cite{position:absolute;left:0;top:408px;width:1200px;text-align:center;color:var(--ink)}
.cite h4{font-size:30px;font-weight:700;margin-bottom:10px}
.cite p{font-size:18px;line-height:26px;width:520px;margin:0 auto}

/* contact */
.contact{position:absolute;left:0;top:2980px;width:1200px;height:432px;background:var(--charcoal-2)}
.contact-shape{position:absolute;inset:0}
.contact h2{position:absolute;left:120px;top:60px;font-size:40px;font-weight:900}
.contact-line{position:absolute;left:120px;display:flex;align-items:center;gap:18px;font-size:22px;font-weight:700}
.contact-line svg{width:30px;height:30px}
.form{position:absolute;left:634px;top:60px;width:446px}
.form h3{font-size:28px;font-weight:400;margin-bottom:16px}
.field{background:var(--white);border:1px solid #ccc;height:34px;margin-bottom:18px;color:#999;font-size:13px;padding:9px 10px}
.row{display:flex;gap:18px}
.row .field{flex:1}
.field.tall{height:110px}
</style>
</head>
<body>
<div class="page">

<header class="hero">
  <svg class="hero-bg" viewBox="0 0 1200 470" preserveAspectRatio="none" aria-hidden="true">
    <polygon points="0,0 1200,0 1200,380 600,470 0,380" fill="#2b2b2b"/>
    <polygon points="0,90 500,300 0,380" fill="#333"/>
    <polygon points="1200,90 700,300 1200,380" fill="#333"/>
  </svg>
  <div class="brand"><span class="brand-square"></span>TALLOW MARSH</div>
  <nav class="nav">
    <a class="active" href="#">HOME</a><a href="#">BLOG</a><a href="#">PRESS</a><a href="#">CONTACT</a>
  </nav>
  <h1 class="headline"><span class="hl">Offensive</span> Services <span class="hl">From</span><br>Offensive <span class="hl">Minds</span></h1>
</header>

<section class="about">
  <svg class="about-shapes" viewBox="0 0 1200 560" preserveAspectRatio="none" aria-hidden="true">
    <polygon points="0,0 600,70 0,70" fill="#2b2b2b"/>
    <polygon points="1200,0 600,70 1200,70" fill="#2b2b2b"/>
    <polygon points="0,70 1200,70 1200,0 1200,560 0,560" fill="#8c8c8c"/>
    <polygon points="0,380 380,560 0,560" fill="#9a9a9a"/>
    <polygon points="1200,300 760,560 1200,560" fill="#999"/>
  </svg>
  <h2>WHAT WE DO</h2>
  <div class="about-copy">
    <p class="lead">We are an information security company focusing on real world threats.</p>
    <p>Tallow Marsh is an information security consulting company that concentrates on the latest threats to organizations today. We perform in-depth analysis, determine organizational/business risk, and find the vulnerabilities before the bad guys do. Our team includes internationally renowned experts who have been featured in international news outlets and conferences, including The Harbor Ledger, The Capital Courier, an Eastline News Documentary.</p>
    <p class="lead">We focus on hacking. This is our passion. We find the vulnerabilities before the bad guys do.</p>
  </div>
  <div class="about-mark"><span class="sq"></span>TALLOW MARSH</div>
</section>

<section class="services">
  <svg class="services-shape" viewBox="0 0 1200 1330" preserveAspectRatio="none" aria-hidden="true">
    <polygon points="0,0 600,40 1200,0 1200,1260 600,1330 0,1260" fill="#ec1f27"/>
    <polygon points="0,0 600,40 1200,0" fill="#8c8c8c"/>
  </svg>
  <h2>SERVICES</h2>
  <div class="grid">
    <article class="card">
      <svg viewBox="0 0 100 100" fill="none" stroke="#fff" stroke-width="10"><path d="M80 50a30 30 0 1 1-9-21"/><polygon points="86,12 86,38 60,38" fill="#fff" stroke="none"/></svg>
      <h3>Internal Pivot Assessment &amp; Post Exploitation</h3>
      <p>We start as a low privilege user and attempt to move through the network in an attempt to access the data that matters to you. This is a simulation of a rogue trusted insider or a compromised internal host. We determine your risk when the egg shell is cracked. Even a seemingly insignificant compromise can have big consequences, and our goal is to demonstrate this risk.</p>
    </article>
    <article class="card">
      <svg viewBox="0 0 100 100" fill="#fff"><circle cx="36" cy="30" r="14"/><path d="M10 82c0-18 12-30 26-30s26 12 26 30z"/><circle cx="68" cy="34" r="11"/><path d="M56 58c4-4 8-6 12-6 12 0 22 10 22 26H64c0-8-3-15-8-20z"/></svg>
      <h3>Red Team Adversary Simulation</h3>
      <p>A goal-based assessment where we attack just like a real world adversary. This includes external attacks and targeted phishing to demonstrate the real risk to your data.</p>
    </article>
    <article class="card">
      <svg viewBox="0 0 100 100" fill="none" stroke="#fff" stroke-width="6"><path d="M20 8h40l16 16v30"/><path d="M20 8v80h36"/><line x1="30" y1="34" x2="60" y2="34"/><line x1="30" y1="48" x2="52" y2="48"/><circle cx="70" cy="70" r="13"/><line x1="80" y1="80" x2="94" y2="94" stroke-width="8"/></svg>
      <h3>Penetration Testing &amp; Vulnerability Assessments</h3>
      <p>This includes vulnerability scans of the in-scope systems where we manually verify issues and exploit any issues found. We report on the issues that actually have a real risk to your organization.</p>
    </article>
    <article class="card">
      <svg viewBox="0 0 100 100" fill="none" stroke="#fff" stroke-width="7"><rect x="12" y="22" width="66" height="66"/><path d="M30 52l16 16 44-50" stroke-width="10"/></svg>
      <h3>Advanced Product, Hardware &amp; RF Testing</h3>
      <p>This is a highly customized assessment designed for you and your hardware. Depending on the product we will analyze custom RF protocols, reverse engineer OS and firmware, and analyze and fuzz network protocols. We have tested a range of products from toys to security products.</p>
    </article>
    <article class="card">
      <svg viewBox="0 0 100 100" fill="none" stroke="#fff" stroke-width="5"><circle cx="50" cy="50" r="40"/><ellipse cx="50" cy="50" rx="17" ry="40"/><line x1="10" y1="50" x2="90" y2="50"/><path d="M16 30h68M16 70h68"/></svg>
      <h3>Web Application Penetration Testing</h3>
      <p>Our team will perform an in-depth analysis of your web application to find vulnerabilities related to programming errors, misconfiguration, and application architectural issues. We will perform automated and manual runtime analysis of your application. We create custom test cases to fuzz your application and find the faults before the bad guys do.</p>
    </article>
    <article class="card">
      <svg viewBox="0 0 100 100" fill="none" stroke="#fff" stroke-width="6"><rect x="28" y="8" width="44" height="84" rx="6"/><line x1="28" y1="76" x2="72" y2="76"/><circle cx="50" cy="84" r="3" fill="#fff"/></svg>
      <h3>Mobile Application Assessment</h3>
      <p>We look at your mobile application and the associated infrastructure to find configuration weaknesses, server-side issues, insecure authentication and access control, and other issues related to the latest attacks on mobile applications.</p>
    </article>
  </div>
</section>

<section class="testimonial">
  <span class="quote-mark left">“</span>
  <span class="quote-mark right">”</span>
  <div class="avatar" role="img" aria-label="Illustrated client avatar"></div>
  <div class="cite">
    <h4>D.H. (Undisclosed Organization)</h4>
    <p>I read the report yesterday. This is one of the best written, actionable pentest reports I've ever seen.</p>
  </div>
</section>

<footer class="contact">
  <svg class="contact-shape" viewBox="0 0 1200 432" preserveAspectRatio="none" aria-hidden="true">
    <polygon points="0,0 1200,0 1200,432 0,432" fill="#343434"/>
    <polygon points="0,0 520,0 0,150" fill="#2e2e2e"/>
  </svg>
  <h2>CONTACT US</h2>
  <div class="contact-line" style="top:142px">
    <svg viewBox="0 0 30 30" fill="none" stroke="#fff" stroke-width="2.5"><rect x="2" y="6" width="26" height="18"/><path d="M2 6l13 11 13-11"/></svg>
    contact@tallowmarsh.com
  </div>
  <div class="contact-line" style="top:196px">
    <svg viewBox="0 0 30 30" fill="#fff"><path d="M7 3l5 6-3 4c2 4 5 7 9 9l4-3 6 5-3 4C14 28 2 16 3 6z"/></svg>
    +1 555-014-2290
  </div>
  <form class="form">
    <h3>Contact Form</h3>
    <div class="field">Company</div>
    <div class="row"><div class="field">Name</div><div class="field">Email Address</div></div>
    <div class="field">Phone Number</div>
    <div class="field tall">Message</div>
  </form>
</footer>

</div>
</body>
</html>
```